Need Primer (paint) Label Design

THE ATTACHED LABEL/S ARE SOLEY FOR REFERENCE. DO NOT MAKE ME AN INTERIOR PAINT OR CHALK PAINT LABEL. I ONLY NEED A "PRIMER" LABEL. THE ATTACHED INTERIOR PAINT LABEL IS ONLY TO SHOW YOU THE THEME/DESIGN OF OUR OTHER LABELS. THE BLUE LABEL ONLY HAS A DESIGN ASPECT I LIKE (PRIMER ON SIDE). The last four labels are our competitors.
```````````````````````````````````````````````````````````````````````````````````````````````````
We need this label to look professional, sharp, eye catching and modern.
OUR PRIMARY COLORS ARE BLACK AND WHITE. IF YOU INCOPORATE ANOTHER COLOR, SILVER OR GOLD MIGHT BE IDEAL BUT PLEASE DON'T DRIFT TOO FAR.
The attached documents:
1st - Our Logo
2nd - Our chalk paint label (reference). We do not need a chalk paint label.
3rd. A random design example. I like the PRIME on the side running vertically. I think it's a cool design concept.
````````````````````````````````````````````````````````````````````````````````````````````````````
We are going to be using a normal paint can with a metal bail/handle so please use that with you design work
``````````````````````````````````````````````````````````````````````````````````````````````````
Order, in my head:
2743
Coatings
^^ I want this to stand out as well but I don't want it to be the first thing your eye is drawn to. Probably 2nd
Interior/Exterior
Multi - Surface Primer
^^ Want this to stick out and draw your eye so the customer knows what it is immediately
Exceptional Adhesion, Performance, Durability,
Use on Wood, Drywall, Plaster, Stucco, Masonry, Brick, Paneling, Painted Metal, & Properly Prepared Glossy Surfaces & More
35* Lowe Temperature Application (can be on side or small)
100% Acrylic
Low Odor - Low VOC - Soap & Water Clean Up
1 US Gallon - 3.785 L
Feel free to get creative with it!

```html
<!DOCTYPE html>
<html lang="en">
<head>
<meta charset="utf-8">
<title>2743 Coatings – Multi-Surface Primer Label</title>
<link href="https://fonts.googleapis.com/css2?family=Montserrat:wght@400;500;700;800;900&display=swap" rel="stylesheet">
<style>
  :root {
    --ink: #000000;
    --paper: #ffffff;
    --backdrop: #f4f4f4;
    --gold: #d4b46a;
    --gold-dark: #7a5028;
    --gold-light: #f1e2b4;
    --grey-text: #222222;
  }
  html, body {
    margin: 0;
    width: 710px;
    height: 1200px;
    overflow: hidden;
    background: var(--backdrop);
    font-family: "Montserrat", sans-serif;
  }
  .label {
    position: absolute;
    left: 25px;
    top: 368px;
    width: 660px;
    height: 464px;
    background: var(--paper);
    box-shadow: 6px 8px 10px rgba(0,0,0,0.25);
    overflow: hidden;
  }
  .brand-panel {
    position: absolute;
    left: 158px;
    top: 0;
    width: 343px;
    height: 360px;
  }
  .brand-panel svg { position: absolute; inset: 0; }
  .brand-name {
    position: absolute;
    left: 0; right: 0; top: 96px;
    margin: 0;
    text-align: center;
    color: var(--paper);
    font-weight: 700;
    font-size: 38px;
    line-height: 1;
    white-space: nowrap;
  }
  .product-type {
    position: absolute; left: 0; right: 0; top: 212px;
    margin: 0;
    text-align: center; color: var(--paper);
    font-weight: 800; font-size: 22px; line-height: 1;
  }
  .product-name {
    position: absolute; left: 0; right: 0; top: 242px;
    margin: 0;
    text-align: center; color: var(--paper);
    font-weight: 400; font-size: 15px; letter-spacing: 0.6px; line-height: 1;
  }
  .benefits {
    position: absolute; left: 44px; right: 44px; top: 272px;
    display: flex; border-top: 1px solid var(--paper);
    color: var(--paper); font-weight: 800; font-size: 8.6px; line-height: 1.15;
    text-align: center;
  }
  .benefits span {
    flex: 1; display: flex; align-items: center; justify-content: center;
    height: 28px; padding-top: 2px;
  }
  .benefits span + span { border-left: 1px solid var(--paper); }
  .spec { position: absolute; left: 38px; color: var(--ink); }
  .spec-temp { top: 162px; }
  .spec-temp .big { font-weight: 900; font-size: 42px; line-height: 1; letter-spacing: -1px; }
  .spec-temp .small { font-size: 11.5px; line-height: 1.1; font-weight: 400; }
  .spec-rule {
    position: absolute; left: 38px; top: 262px; width: 98px; height: 3px;
    background: linear-gradient(90deg, var(--gold-dark), var(--gold-light) 45%, var(--gold) 70%, var(--gold-dark));
  }
  .spec-acrylic { top: 274px; }
  .spec-acrylic .big { font-weight: 900; font-size: 30px; line-height: 1; }
  .spec-acrylic .small { font-size: 21px; line-height: 1; font-weight: 400; }
  .size-tag { position: absolute; left: 37px; top: 389px; width: 95px; height: 75px; }
  .size-tag svg { position: absolute; inset: 0; }
  .size-tag p {
    position: relative; margin: 0; padding-top: 20px;
    text-align: center; color: var(--paper); font-weight: 700; font-size: 11px; line-height: 1.25;
  }
  .features {
    position: absolute; left: 158px; width: 343px; top: 377px; margin: 0;
    text-align: center; color: var(--ink);
    font-weight: 800; font-size: 11.4px; white-space: nowrap;
  }
  .surfaces {
    position: absolute; left: 150px; width: 360px; top: 404px; margin: 0;
    text-align: center; color: var(--grey-text);
    font-size: 7.8px; line-height: 1.55; font-weight: 500;
  }
  .category-word {
    position: absolute; left: 536px; top: 28px; height: 408px;
    margin: 0;
    writing-mode: vertical-rl; transform: rotate(180deg);
    font-weight: 800; font-size: 100px; line-height: 1; color: var(--ink);
    letter-spacing: -2px; text-align: center;
  }
</style>
</head>
<body>
  <main class="label">
    <section class="brand-panel">
      <svg viewBox="0 0 343 360" width="343" height="360" aria-hidden="true">
        <defs>
          <linearGradient id="goldBand" x1="0" x2="1" y1="0" y2="0">
            <stop offset="0" stop-color="#6e4420"/>
            <stop offset="0.38" stop-color="#c9a86a"/>
            <stop offset="0.4" stop-color="#f3e6bd"/>
            <stop offset="0.7" stop-color="#c8a866"/>
            <stop offset="1" stop-color="#6e4420"/>
          </linearGradient>
        </defs>
        <path d="M0 332 Q171.5 375 343 332 L343 346 Q171.5 389 0 346 Z" fill="url(#goldBand)"/>
        <path d="M0 0 H343 V332 Q171.5 372 0 332 Z" fill="#000"/>
      </svg>
      <p class="brand-name">2743 Coatings</p>
      <p class="product-type">INTERIOR/EXTERIOR</p>
      <p class="product-name">MULTI - SURFACE PRIMER</p>
      <div class="benefits">
        <span>EXCEPTIONAL<br>ADHESION</span>
        <span>PERFORMANCE</span>
        <span>DURABILITY</span>
      </div>
    </section>

    <div class="spec spec-temp">
      <div class="big">35*</div>
      <div class="small">LOWE<br>TEMPERATURE<br>APPLICATION</div>
    </div>
    <div class="spec-rule"></div>
    <div class="spec spec-acrylic">
      <div class="big">100%</div>
      <div class="small">ACRYLIC</div>
    </div>

    <div class="size-tag">
      <svg viewBox="0 0 95 75" width="95" height="75" aria-hidden="true">
        <path d="M0 6 Q47.5 -4 95 6 V75 H0 Z" fill="#000"/>
      </svg>
      <p>1 US Gallon<br>3.785 L</p>
    </div>

    <p class="features">LOW ODOR - LOW VOC - SOAP &amp; WATER CLEAN UP</p>
    <p class="surfaces">
      USE ON WOOD &nbsp;·&nbsp; DRYWALL &nbsp;·&nbsp; PLASTER &nbsp;·&nbsp; STUCCO &nbsp;·&nbsp; MASONRY &nbsp;·<br>
      BRICK &nbsp;·&nbsp; PANELING &nbsp;·&nbsp; PAINTED METAL &nbsp;·&nbsp; &amp; PROPERLY<br>
      PREPARED GLOSSY SURFACES &amp; MORE
    </p>

    <p class="category-word">Primer</p>
  </main>
</body>
</html>
```